Portrait Photographer Newsletter (www.lakesidelensworks.com)

We would like a newsletter that can be used in Mailbright Hub....you can visit our website to get some content....The main topics for the newsletter are 1. planning for your family portraits 2. We also offer restoration of your family heirlooms 3. Coming Soon.....www.dockandcottageguard.com (get content off our website.)
Misc:
Gift Certificates are available.
Click to schedule you appt today.
Mothers day.
I can provide more pictures but we really need the content of the news letter- we need a good writer...feel free to use info our of our website or be creative :)
We need help keeping up with email marketing if we find a fit, we would like to use find someone to help with this weekly or monthly
Target Market(s)
Family, middle to upper class
Industry/Entity Type
Portrait Photography
Designer to choose colors to be used in the design.

```html
<!DOCTYPE html>
<html lang="en">
<head>
<meta charset="utf-8">
<title>Lakeside Lens Works Newsletter</title>
<link href="https://fonts.googleapis.com/css2?family=Bree+Serif&family=Roboto+Condensed:wght@400;700&family=Arimo:wght@400&display=swap" rel="stylesheet">
<style>
  :root {
    --navy: #23254f;
    --navy-line: #2a2f5a;
    --blue: #1e8fd0;
    --band-blue: #2aa0dc;
    --sand: #c8a672;
    --sky-top: #dfe9f1;
    --sky-bottom: #b9cfdf;
    --page: #eef0f2;
    --text: #3b3b3b;
    --white: #ffffff;
  }
  * { box-sizing: border-box; margin: 0; padding: 0; }
  html, body { width: 1200px; height: 806px; overflow: hidden; background: var(--page); }
  .newsletter {
    position: absolute; left: 426px; top: 19px;
    width: 434px; height: 960px;
    transform: scale(0.8); transform-origin: top left;
    background: var(--white);
    box-shadow: 0 2px 12px rgba(0,0,0,.12);
    font-family: "Arimo", Arial, sans-serif;
    overflow: hidden;
  }
  .hero { position: absolute; left: 0; top: 0; width: 434px; height: 262px;
    background: linear-gradient(180deg, var(--sky-top) 0%, var(--sky-bottom) 62%, #d9c39a 80%, var(--sand) 100%); }
  .brand { position: absolute; left: 24px; top: 14px; display: flex; align-items: center; gap: 6px; }
  .brand-dot { width: 10px; height: 10px; border-radius: 50%; background: var(--navy); }
  .brand-name { font-family: "Bree Serif", serif; font-size: 17px; color: var(--navy); line-height: 1; }
  .brand-tag { position: absolute; left: 40px; top: 38px; font-size: 4px; letter-spacing: .5px; color: var(--navy); }
  .social-badge { position: absolute; left: 334px; top: 28px; width: 73px; height: 22px;
    background: #3b5fa8; border-radius: 3px; color: var(--white);
    font-family: "Roboto Condensed", sans-serif; font-size: 8px; display: flex; align-items: center; justify-content: center; }
  .promo-box { position: absolute; left: 22px; top: 290px; width: 392px; height: 39px;
    border: 2px solid var(--navy-line); text-align: center; }
  .promo-kicker { position: absolute; left: 50%; top: -11px; transform: translateX(-50%);
    background: var(--white); padding: 0 6px; font-family: "Bree Serif", serif; font-size: 14px; color: var(--blue); white-space: nowrap; }
  .promo-line { margin-top: 10px; font-family: "Bree Serif", serif; font-size: 15px; color: var(--blue); white-space: nowrap; }
  .feature-photo { position: absolute; left: 22px; top: 352px; width: 170px; height: 165px; border-radius: 18px;
    background: linear-gradient(180deg, #4b6b96 0%, #2e3f60 40%, #c9803a 62%, #5a3a1e 100%); }
  .feature-title { position: absolute; left: 205px; top: 360px; width: 215px;
    font-family: "Roboto Condensed", sans-serif; font-weight: 700; font-size: 17px; line-height: 18px; color: var(--navy); }
  .feature-body { position: absolute; left: 205px; top: 404px; width: 208px;
    font-size: 8px; line-height: 10.4px; color: var(--text); text-align: justify; }
  .feature-body p + p { margin-top: 11px; }
  .thumbs { position: absolute; left: 22px; top: 543px; display: flex; gap: 10px; }
  .thumb { width: 70px; height: 76px; border: 1.5px solid var(--blue); }
  .thumb-1 { background: linear-gradient(180deg, #e9b9a5, #5b6a7a); }
  .thumb-2 { background: linear-gradient(180deg, #a7bccb, #6a6a6e); }
  .thumb-3 { background: linear-gradient(180deg, #8fb6d5, #c9c19b); }
  .thumb-4 { background: linear-gradient(180deg, #b23a3a, #4f4a4d); }
  .thumb-5 { background: linear-gradient(180deg, #a9c5db, #dde6ec); }
  .offer-band { position: absolute; left: 0; top: 633px; width: 434px; height: 92px; background: var(--band-blue); }
  .offer-box { position: absolute; left: 15px; top: 28px; width: 405px; height: 46px; border: 1.5px solid var(--white);
    color: var(--white); text-align: center; font-size: 12px; padding-top: 17px; }
  .offer-title { position: absolute; left: 50%; top: -14px; transform: translateX(-50%);
    background: var(--band-blue); padding: 0 10px; font-family: "Bree Serif", serif; font-size: 20px; white-space: nowrap; }
  .actions { position: absolute; left: 40px; top: 744px; display: flex; gap: 42px; }
  .action { width: 90px; height: 90px; border-radius: 50%; display: flex; align-items: center; justify-content: center;
    text-align: center; color: var(--white); font-family: "Roboto Condensed", sans-serif; font-size: 11px; line-height: 12px;
    background: radial-gradient(circle at 50% 25%, #4b4d7e 0%, var(--navy) 55%); box-shadow: 0 3px 4px rgba(0,0,0,.25); }
  .action-primary { background: radial-gradient(circle at 50% 25%, #6fc6ee 0%, var(--band-blue) 55%); }
  .footer { position: absolute; left: 0; top: 850px; width: 434px; height: 110px; background: var(--navy); text-align: center; color: var(--white); }
  .footer-title { margin-top: 24px; font-family: "Roboto Condensed", sans-serif; font-weight: 700; font-size: 19px; line-height: 22px; color: var(--band-blue); }
  .footer-text { font-size: 10.5px; line-height: 12.5px; padding: 0 18px; }
  .footer-url { margin-top: 8px; font-size: 14.5px; }
</style>
</head>
<body>
<main class="newsletter">
  <header class="hero" role="img" aria-label="Family jumping together on a sunny beach">
    <div class="brand"><span class="brand-dot"></span><span class="brand-name">Lakeside Lens Works</span></div>
    <div class="brand-tag">ARTISTIC PORTRAITS FAMILY HEIRLOOMS</div>
    <div class="social-badge">Follow on Socialine</div>
  </header>

  <section class="promo-box">
    <span class="promo-kicker">Trust Dock &amp; Cottage</span>
    <p class="promo-line">Guard will keep a careful eye on your property!</p>
  </section>

  <div class="feature-photo" role="img" aria-label="Lit beach gazebo at sunset"></div>
  <h2 class="feature-title">PLANNING FOR YOUR<br>FAMILY PORTRAITS</h2>
  <div class="feature-body">
    <p>Lorem ipsum dolor sit amet, consectetur adipiscing elit, sed do eiusmod tempor incididunt ut labore et dolore magna aliqua. Ut enim ad minim veniam,</p>
    <p>quis nostrud exercitation ullamco laboris nisi ut aliquip ex ea commodo consequat. Duis aute irure dolor in reprehenderit in voluptate velit esse cillum dolore eu fugiat nulla pariatur. Excepteur sint occaecat cupidatat non ui officia deserunt mollit anim id est laborum.</p>
  </div>

  <div class="thumbs">
    <div class="thumb thumb-1" role="img" aria-label="Family on the beach at dusk"></div>
    <div class="thumb thumb-2" role="img" aria-label="Children posing by the shore"></div>
    <div class="thumb thumb-3" role="img" aria-label="Child sitting in dune grass"></div>
    <div class="thumb thumb-4" role="img" aria-label="Couple by a red building"></div>
    <div class="thumb thumb-5" role="img" aria-label="Toddler with birthday cake on the beach"></div>
  </div>

  <section class="offer-band">
    <div class="offer-box">
      <span class="offer-title">WE OFFER</span>
      WE ALSO OFFER RESTORATION OF YOUR FAMILY HEIRLOOMS
    </div>
  </section>

  <nav class="actions">
    <div class="action">Gift Certificates<br>are available.</div>
    <div class="action action-primary">Click to schedule<br>you appt today</div>
    <div class="action">Mothers day</div>
  </nav>

  <footer class="footer">
    <h2 class="footer-title">SCHEDULE AN APPOINTMENT</h2>
    <p class="footer-text">with us to learn about how we can protect your beach home while you are<br>away- our new business:</p>
    <p class="footer-url">www.dockandcottageguard.com</p>
  </footer>
</main>
</body>
</html>
```